Brixelo Photography Business Cards

We need a good general business card that we can hand to our clients. We will be doing embossed gloss cards.

Target Market(s)

Real estate / Business to business / professionals

```html
<!DOCTYPE html>
<html lang="en">
<head>
<meta charset="utf-8">
<title>Brixelo Photography Business Cards</title>
<link rel="stylesheet" href="https://fonts.googleapis.com/css2?family=Open+Sans:wght@400;600;700&display=swap">
<style>
  :root {
    --backdrop: #aeb1b5;
    --card: #dcd6e3;
    --navy: #2b2d5e;
    --sky: #3aa9e0;
  }
  * { box-sizing: border-box; margin: 0; padding: 0; }
  html, body { width: 1200px; height: 900px; overflow: hidden; }
  body {
    background: var(--backdrop);
    font-family: "Open Sans", Arial, sans-serif;
    color: var(--navy);
    position: relative;
  }
  .card {
    position: absolute;
    top: 300px;
    width: 520px;
    height: 300px;
    background: var(--card);
  }
  .card--front { left: 60px; }
  .card--back { left: 620px; display: flex; align-items: center; justify-content: center; }

  .person { position: absolute; left: 36px; top: 34px; width: 300px; }
  .person__name { font-size: 40px; font-weight: 700; line-height: 1.1; white-space: nowrap; }
  .person__title { font-size: 12px; text-align: right; letter-spacing: 0.5px; margin-top: 2px; }
  .person__rule { height: 2px; background: var(--navy); margin-top: 8px; }

  .contact { position: absolute; left: 90px; top: 160px; }
  .contact__heading { font-size: 18px; font-weight: 700; letter-spacing: 1px; margin-bottom: 16px; }
  .contact__line { font-size: 14px; line-height: 1.5; }

  .brand-stamp { position: absolute; right: 24px; bottom: 36px; display: flex; align-items: center; gap: 10px; }
  .brand-stamp__circle { width: 44px; height: 44px; border: 3px solid var(--navy); border-radius: 50%; }
  .brand-stamp__name { font-size: 16px; font-weight: 700; color: var(--navy); }

  .brand-main { font-size: 44px; font-weight: 700; color: var(--navy); text-align: center; line-height: 1.1; }
</style>
</head>
<body>
  <section class="card card--front">
    <div class="person">
      <h1 class="person__name">Name Nameson</h1>
      <p class="person__title">JOB TITLE</p>
      <div class="person__rule"></div>
    </div>
    <div class="contact">
      <h2 class="contact__heading">CONTACT</h2>
      <p class="contact__line">(555) 555-1234</p>
      <p class="contact__line">www.website.com</p>
    </div>
    <div class="brand-stamp">
      <span class="brand-stamp__circle"></span>
      <span class="brand-stamp__name">Brixelo Photography</span>
    </div>
  </section>

  <section class="card card--back">
    <p class="brand-main">Brixelo<br>Photography</p>
  </section>
</body>
</html>
```